1 Home page redesign for existing repair service site.

We need a refresh of our existing website that looks more 2017. We have made a mockup of the content that we want and a sample of where we want it. Nothing is set in stone, if you have better ideas of where things should go, feel free.

You can see our current site at http://www.fixoloda.gr

The colors should stay orange/black/grey.

In many of the "boxes/banners" we will need images. Feel free to find in pixel vault as we have an account.

We have made notes throughout the wireframe that we have attached on what we are looking for. Let us know if you have any questions. Thanks.

Target Market(s)

People using technology and breaking it

Industry/Entity Type

It Service

Number of Pages Required

1 page

Font styles to use
Sans Serif

Requirements
Must have
• Must have a modern, professional look and feel. Need custom graphics and icons.

```html
<!DOCTYPE html>
<html lang="en">
<head>
<meta charset="utf-8">
<title>Fixoloda – Device Repair</title>
<link href="https://fonts.googleapis.com/css?family=Open+Sans:400,600,700,800&display=swap" rel="stylesheet">
<style>
:root{
  --orange:#f07c1b;
  --orange-dark:#d9650a;
  --ink:#222;
  --charcoal:#2c2c2c;
  --slate:#3b3b3b;
  --grey:#777;
  --line:#dcdcdc;
  --paper:#f3f3f3;
  --white:#fff;
}
*{box-sizing:border-box;margin:0;padding:0}
html,body{width:1200px;height:3228px;overflow:hidden}
body{font-family:"Open Sans",Arial,sans-serif;color:var(--ink);background:var(--white);position:relative;font-size:13px}
.abs{position:absolute}
svg{display:block}

/* top bar */
.topbar{top:0;left:0;width:1200px;height:28px;background:var(--charcoal);color:#ccc;font-size:11px}
.topbar .quick{left:60px;top:5px;width:110px;height:18px;background:#444;padding:1px 8px;border-radius:2px}
.topbar .lang{right:60px;top:6px;display:flex;gap:12px}
/* nav */
.nav{top:28px;left:0;width:1200px;height:112px;background:var(--white);border-bottom:1px solid var(--line)}
.logo{left:60px;top:34px;display:flex;align-items:center;gap:10px;font-size:34px;font-weight:700;color:var(--ink)}
.logo .mark{width:30px;height:30px;background:var(--orange);border-radius:4px}
.menu{left:400px;top:44px;display:flex;gap:46px;font-weight:700;font-size:14px;color:var(--ink)}
.menu span{border-bottom:3px solid transparent;padding-bottom:6px}
.menu span:first-child{border-color:var(--orange)}
.phone{left:820px;top:34px;color:var(--orange);font-weight:700;font-size:18px;line-height:1.1}
.phone small{display:block;color:var(--grey);font-weight:400;font-size:11px}
.chat{left:990px;top:34px;color:var(--orange);font-weight:700;font-size:18px;line-height:1.1}
.chat small{display:block;color:var(--grey);font-weight:400;font-size:11px}
.social{display:flex;gap:6px}
.social i{width:22px;height:22px;border-radius:50%;background:#bbb;display:block}
.nav .social{left:1080px;top:44px}

/* hero */
.hero{top:140px;left:0;width:1200px;height:400px;background:linear-gradient(135deg,#6d6d6d 0%,#3c3c3c 45%,#1e1e1e 100%)}
.play{left:680px;top:160px;width:80px;height:80px;border-radius:50%;background:rgba(255,255,255,.85)}
.hero h1{left:40px;top:300px;font-size:58px;font-weight:800;color:var(--white);letter-spacing:1px;line-height:1}
.hero p{left:40px;top:360px;font-size:32px;color:var(--orange);font-weight:600}
.counter{top:540px;left:0;width:1200px;height:60px;background:#111;display:flex;align-items:center;padding-left:40px;gap:6px}
.counter b{width:38px;height:44px;background:var(--white);color:var(--ink);font-size:30px;font-weight:800;display:flex;align-items:center;justify-content:center}
.counter span{color:var(--white);font-size:21px;margin-left:14px}

/* banners */
.banner{top:600px;width:600px;height:328px}
.banner.loc{left:0;background:linear-gradient(160deg,#e8e4df,#b7c2c9 60%,#8c8f94)}
.banner.price{left:600px;background:linear-gradient(160deg,#d8d6d3,#b9a9a0 55%,#7e7470)}
.banner .cap{left:0;bottom:0;width:600px;height:92px;background:rgba(20,20,20,.78);padding:16px 30px;color:var(--white)}
.cap h2{font-size:24px;font-weight:700}
.cap p{font-size:13px;color:#ddd}
.cap a{font-size:11px;color:var(--orange);text-decoration:none}

/* features */
.features{top:990px;left:60px;width:1080px;display:flex;gap:20px}
.feature{width:255px;height:225px;background:var(--paper);border:1px solid var(--line);padding:14px;position:relative}
.feature .ico{width:26px;height:26px}
.feature h3{font-size:12px;font-weight:700;margin:10px 0 6px;width:120px}
.feature p{font-size:9px;color:var(--grey);width:120px;line-height:1.4}
.feature .more{position:absolute;left:14px;bottom:20px;font-size:9px;border:1px solid #bbb;background:var(--white);padding:4px 10px}
.feature .pic{position:absolute;right:12px;top:14px;width:105px;height:180px;background:linear-gradient(180deg,#d2d2d2,#b0b0b0)}

/* section titles */
.title{left:0;width:1200px;text-align:center;color:var(--orange);font-weight:800;font-size:22px;letter-spacing:1px}
.title::before,.title::after{content:"";display:inline-block;width:50px;height:2px;background:var(--orange);vertical-align:middle;margin:0 16px}

/* repair grid */
.repairs{top:1380px;left:140px;width:920px;display:grid;grid-template-columns:repeat(5,1fr);row-gap:70px}
.device{text-align:center;font-size:12px}
.device svg{margin:0 auto 14px;height:70px;width:80px}

/* options band */
.options{top:1720px;left:0;width:1200px;height:160px;background:var(--slate);color:var(--white)}
.options h2{position:absolute;top:30px;width:1200px;text-align:center;font-size:20px;font-weight:700}
.opt-row{position:absolute;top:90px;left:160px;width:880px;display:flex;justify-content:space-between;font-size:16px}
.opt-row div{display:flex;align-items:center;gap:10px}

/* why choose */
.why{top:2000px;left:120px;width:960px;display:flex;gap:8px}
.why-card{width:234px}
.why-card .pic{height:210px;position:relative}
.why-card .lbl{background:#1d1d1d;color:var(--white);font-size:12px;padding:8px 10px}
.badge{position:absolute;left:47px;top:35px;width:140px;height:140px;border-radius:50%;background:#d4a62a;border:8px solid #222}
.arrow{width:22px;height:50px;background:#bbb}

/* testimonials */
.stars{top:2330px;left:0;width:1200px;display:flex;justify-content:center;gap:6px}
.reviews{top:2380px;left:120px;width:960px;display:flex;gap:24px}
.review{width:222px}
.review h4{color:var(--orange);font-size:13px;font-weight:600}
.review .sub{font-size:10px;color:var(--grey);margin-bottom:8px}
.review .box{border:1px solid var(--line);height:190px;padding:14px;font-size:10px;color:var(--grey);line-height:1.6;position:relative}
.review .who{position:absolute;right:14px;bottom:12px;font-size:10px;color:var(--ink)}
.cta{top:2660px;left:510px;width:180px;height:28px;border:1px solid #bbb;background:var(--paper);font-size:10px;text-align:center;line-height:26px;color:#555}

/* footer */
.foot{top:2760px;left:0;width:1200px;height:260px;background:var(--paper);border-top:1px solid var(--line)}
.fcol{top:30px;font-size:10px;color:var(--grey);line-height:2}
.fcol h5{color:var(--orange);font-size:14px;font-weight:600;margin-bottom:6px}
.fcol .post{margin-bottom:10px;line-height:1.4}
.fcol .post b{color:var(--ink);display:block;font-weight:600}
.input{width:260px;height:28px;background:var(--white);border:1px solid var(--line);display:flex;justify-content:flex-end}
.input i{width:60px;background:#ddd}
.foot .social i{width:18px;height:18px;background:#999}
.footdark{top:3020px;left:0;width:1200px;height:150px;background:var(--slate);color:var(--white)}
.fd{position:absolute;top:40px;display:flex;gap:10px;font-size:14px}
.fd small{display:block;color:var(--orange);font-size:10px}
.copy{top:3170px;left:0;width:1200px;height:58px;background:#1c1c1c;color:#888;font-size:10px;padding:20px 60px}
.livechat{top:3196px;left:960px;width:180px;height:32px;background:var(--orange);color:var(--white);font-weight:700;font-size:13px;padding:7px 14px}
</style>
</head>
<body>

<div class="abs topbar">
  <div class="abs quick">Quick Links ▾</div>
  <div class="abs lang"><span>EN</span><span>GR</span><span>Help</span></div>
</div>

<header class="abs nav">
  <div class="abs logo"><span class="mark"></span>Fixoloda</div>
  <nav class="abs menu"><span>REPAIRS</span><span>20 STORES</span><span>BLOG</span></nav>
  <div class="abs phone">210 555 0142<small>24/7 service available</small></div>
  <div class="abs chat">Live Chat<small>With Us</small></div>
  <div class="abs social"><i></i><i></i><i></i></div>
</header>

<section class="abs hero" role="img" aria-label="Technicians repairing devices in the open service area">
  <div class="abs play"><svg width="80" height="80" viewBox="0 0 80 80"><path d="M32 24 L58 40 L32 56Z" fill="#222"/></svg></div>
  <h1 class="abs">OPEN SERVICE AREA</h1>
  <p class="abs">you can see your device being repaired</p>
</section>

<div class="abs counter"><b>9</b><b>3</b><b>7</b><b>2</b><b>6</b><span>Repairs completed with happy customers. Yep, we fix a lot of devices!</span></div>

<section class="abs banner loc" role="img" aria-label="City map with location pins">
  <div class="abs cap"><h2>20 FIXOLODA LOCATIONS</h2><p>Find a Store Near You</p><a>See Map</a></div>
</section>
<section class="abs banner price" role="img" aria-label="Hand dropping a coin into a piggy bank">
  <div class="abs cap"><h2>LOW PRICE GUARANTEE</h2><p>Find a lower price for your Smartphone Repair? We will match it!</p><a>See details and terms</a></div>
</section>

<div class="abs features">
  <div class="feature"><svg class="ico" viewBox="0 0 26 26"><path d="M2 13 Q13 3 24 13 Q13 23 2 13Z" fill="none" stroke="#222" stroke-width="2"/><circle cx="13" cy="13" r="4" fill="#222"/></svg><h3>OPEN SERVICE AREA</h3><p>Watch our team repair your device right in front of you.</p><span class="more">Read more</span><div class="pic" role="img" aria-label="Service area photo"></div></div>
  <div class="feature"><svg class="ico" viewBox="0 0 26 26"><path d="M3 3 H13 L23 13 L13 23 L3 13Z" fill="#222"/><circle cx="8" cy="8" r="2" fill="#fff"/></svg><h3>SAVE 20-70% ON MULTIPLE REPAIRS</h3><p>Bundle your repairs and pay much less for each one.</p><span class="more">Read more</span><div class="pic" role="img" aria-label="Devices on a workbench"></div></div>
  <div class="feature"><svg class="ico" viewBox="0 0 26 26"><rect x="3" y="6" width="20" height="16" rx="2" fill="#222"/><rect x="9" y="2" width="8" height="6" fill="none" stroke="#222" stroke-width="2"/></svg><h3>ACCESSORIES</h3><p>Cases, chargers and screen guards for every device.</p><span class="more">Read more</span><div class="pic" role="img" aria-label="Accessories on display"></div></div>
  <div class="feature"><svg class="ico" viewBox="0 0 26 26"><circle cx="13" cy="13" r="10" fill="none" stroke="#222" stroke-width="2.5"/><path d="M13 7 V13 L17 16" stroke="#222" stroke-width="2.5" fill="none"/></svg><h3>20 MINUTE REPAIRS</h3><p>Most screen and battery jobs done while you wait.</p><span class="more">Read more</span><div class="pic" role="img" aria-label="Technician at work"></div></div>
</div>

<h2 class="abs title" style="top:1318px">WHAT WE REPAIR</h2>
<div class="abs repairs">
  <div class="device"><svg viewBox="0 0 80 70"><rect x="28" y="4" width="24" height="62" rx="4" fill="none" stroke="#222" stroke-width="3"/><circle cx="40" cy="58" r="2.5" fill="#222"/></svg>Smartphone Repair</div>
  <div class="device"><svg viewBox="0 0 80 70"><rect x="18" y="4" width="44" height="62" rx="4" fill="none" stroke="#222" stroke-width="3"/><circle cx="40" cy="59" r="2.5" fill="#222"/></svg>Tablet Repair</div>
  <div class="device"><svg viewBox="0 0 80 70"><rect x="30" y="6" width="20" height="58" rx="4" fill="none" stroke="#222" stroke-width="3"/><circle cx="40" cy="56" r="2.5" fill="#222"/></svg>Music Player Repair</div>
  <div class="device"><svg viewBox="0 0 80 70"><rect x="27" y="4" width="26" height="62" rx="6" fill="none" stroke="#222" stroke-width="3"/><line x1="35" y1="60" x2="45" y2="60" stroke="#222" stroke-width="3"/></svg>Handset Repair</div>
  <div class="device"><svg viewBox="0 0 80 70"><rect x="26" y="4" width="28" height="62" rx="4" fill="none" stroke="#222" stroke-width="3"/><rect x="31" y="9" width="18" height="24" fill="#222"/><g fill="#222"><rect x="31" y="40" width="4" height="3"/><rect x="38" y="40" width="4" height="3"/><rect x="45" y="40" width="4" height="3"/><rect x="31" y="47" width="4" height="3"/><rect x="38" y="47" width="4" height="3"/><rect x="45" y="47" width="4" height="3"/></g></svg>Keypad Phone Repair</div>
  <div class="device"><svg viewBox="0 0 80 70"><rect x="8" y="6" width="64" height="42" rx="2" fill="none" stroke="#222" stroke-width="3"/><path d="M34 48 L32 62 H48 L46 48" fill="none" stroke="#222" stroke-width="3"/></svg>Desktop Repair</div>
  <div class="device"><svg viewBox="0 0 80 70"><rect x="14" y="12" width="52" height="36" rx="2" fill="none" stroke="#222" stroke-width="3"/><path d="M4 54 H76 L72 60 H8Z" fill="#222"/></svg>Notebook Repair</div>
  <div class="device"><svg viewBox="0 0 80 70"><rect x="8" y="6" width="50" height="36" fill="none" stroke="#222" stroke-width="3"/><rect x="62" y="10" width="12" height="52" fill="none" stroke="#222" stroke-width="3"/><line x1="24" y1="56" x2="44" y2="56" stroke="#222" stroke-width="3"/></svg>Computer Repair</div>
  <div class="device"><svg viewBox="0 0 80 70"><rect x="16" y="10" width="48" height="34" fill="none" stroke="#222" stroke-width="3"/><path d="M6 50 H74 L70 58 H10Z" fill="none" stroke="#222" stroke-width="3"/></svg>Laptop Repair</div>
  <div class="device"><svg viewBox="0 0 80 70"><circle cx="40" cy="18" r="10" fill="#222"/><path d="M20 64 Q20 34 40 34 Q60 34 60 64Z" fill="#222"/></svg>Business Services</div>
</div>

<section class="abs options">
  <h2>REPAIR OPTIONS</h2>
  <div class="opt-row">
    <div><svg width="18" height="24" viewBox="0 0 18 24"><path d="M9 0 C3 0 0 4 0 8 C0 14 9 24 9 24 S18 14 18 8 C18 4 15 0 9 0Z" fill="#fff"/><circle cx="9" cy="8" r="3" fill="#3b3b3b"/></svg>Find a store near you <span style="color:var(--orange)">?</span></div>
    <div><svg width="24" height="20" viewBox="0 0 24 20"><path d="M0 10 L24 0 L18 20 L11 13Z" fill="#fff"/></svg>Send us your device <span style="color:var(--orange)">?</span></div>
    <div><svg width="28" height="20" viewBox="0 0 28 20"><rect x="0" y="3" width="17" height="12" fill="#fff"/><path d="M17 7 H23 L27 11 V15 H17Z" fill="#fff"/><circle cx="6" cy="17" r="3" fill="#fff"/><circle cx="22" cy="17" r="3" fill="#fff"/></svg>Free pickup in Athens <span style="color:var(--orange)">?</span></div>
  </div>
</section>

<h2 class="abs title" style="top:1940px">WHY CHOOSE FIXOLODA</h2>
<div class="abs arrow" style="top:2090px;left:84px"></div>
<div class="abs arrow" style="top:2090px;left:1094px"></div>
<div class="abs why">
  <div class="why-card"><div class="pic" style="background:#161616" role="img" aria-label="Lifetime guarantee seal"><span class="badge"></span></div><div class="lbl">Lifetime Guarantee</div></div>
  <div class="why-card"><div class="pic" style="background:linear-gradient(150deg,#c7c9cc,#6d7884)" role="img" aria-label="Circuit board being soldered"></div><div class="lbl">Chip-Level Repairs</div></div>
  <div class="why-card"><div class="pic" style="background:linear-gradient(150deg,#2a5fa8,#0f2247)" role="img" aria-label="Hand holding a phone with a privacy shield"></div><div class="lbl">Personal Privacy Protected</div></div>
  <div class="why-card"><div class="pic" style="background:linear-gradient(150deg,#cfd7de,#5e6a74)" role="img" aria-label="Technician using precision tools"></div><div class="lbl">Expert Technicians</div></div>
</div>

<h2 class="abs title" style="top:2288px">WHAT OUR CUSTOMERS SAY</h2>
<div class="abs stars">
  <svg width="150" height="26" viewBox="0 0 150 26"><g fill="#f07c1b"><path id="st" d="M13 1 L16.5 9 L25 9.5 L18.5 15 L20.5 24 L13 19 L5.5 24 L7.5 15 L1 9.5 L9.5 9Z"/><use href="#st" x="31"/><use href="#st" x="62"/><use href="#st" x="93"/><use href="#st" x="124"/></g></svg>
</div>
<div class="abs arrow" style="top:2470px;left:90px;width:16px;height:40px"></div>
<div class="abs arrow" style="top:2470px;left:1094px;width:16px;height:40px"></div>
<div class="abs reviews">
  <div class="review"><h4>Laptop Repair</h4><div class="sub">Overheating</div><div class="box">“My laptop kept shutting down from the heat. They cleaned it, replaced the paste and it runs cool and quiet again. Fast, friendly and fairly priced.”<span class="who"><b>John Coe</b>, Marousi</span></div></div>
  <div class="review"><h4>Laptop Repair</h4><div class="sub">Overheating</div><div class="box">“I watched the whole repair through the glass. Clear quote up front, no surprises at the counter, and my machine was ready the same afternoon.”<span class="who"><b>John Coe</b>, Marousi</span></div></div>
  <div class="review"><h4>Laptop Repair</h4><div class="sub">Overheating</div><div class="box">“The fan was grinding and the case burned my hands. Now it is silent. The staff explained every step and gave me tips to keep it clean.”<span class="who"><b>John Coe</b>, Marousi</span></div></div>
  <div class="review"><h4>Laptop Repair</h4><div class="sub">Overheating</div><div class="box">“Second time I have used them and once again great service. Quick diagnosis, honest advice and a lifetime guarantee on the work.”<span class="who"><b>John Coe</b>, Marousi</span></div></div>
</div>
<div class="abs cta">Visit a Local Repair Department</div>

<footer class="abs foot">
  <div class="abs fcol" style="left:60px"><h5>Quick Links</h5>
    <div style="display:flex;gap:60px"><div>Screen Repairs<br>Battery Swaps<br>Data Recovery<br>Store Finder<br>Gift Cards</div><div>Shipping Information<br>Terms of Service<br>Privacy and Cookies Policy<br>Careers</div></div></div>
  <div class="abs fcol" style="left:470px;width:280px"><h5>Fixoloda Blog</h5>
    <div class="post"><b>20 year old learns to fix phones</b>from scratch and opens a shop</div>
    <div class="post"><b>20 year old learns to fix phones</b>from scratch and opens a shop</div>
    <div class="post"><b>20 year old learns to fix phones</b>from scratch and opens a shop</div></div>
  <div class="abs fcol" style="left:880px"><h5>Newsletter Sign Up</h5>
    <div class="input"><i></i></div>
    <h5 style="margin-top:22px">Social</h5>
    <div class="social"><i></i><i></i><i></i><i></i><i></i><i></i></div></div>
</footer>

<section class="abs footdark">
  <div class="fd" style="left:60px"><svg width="28" height="20" viewBox="0 0 28 20"><rect x="1" y="1" width="26" height="18" fill="none" stroke="#fff" stroke-width="2"/><path d="M1 1 L14 11 L27 1" fill="none" stroke="#fff" stroke-width="2"/></svg><div>Email Support<small>Click to send email</small></div></div>
  <div class="fd" style="left:470px"><svg width="22" height="22" viewBox="0 0 22 22"><path d="M4 1 L9 6 L6 9 Q9 14 13 16 L16 13 L21 18 L17 21 Q6 19 1 5Z" fill="#fff"/></svg><div>Contact our call center<small>210 555 0142</small></div></div>
  <div class="fd" style="left:880px"><svg width="24" height="22" viewBox="0 0 24 22"><path d="M2 2 H22 V15 H10 L5 20 V15 H2Z" fill="#fff"/></svg><div>LIVE CHAT<small>Click to chat now</small></div></div>
</section>
<div class="abs copy">Copyright © 2017 · Fixoloda.gr · All rights reserved.</div>
<div class="abs livechat">Fixoloda Live Chat ▴</div>

</body>
</html>
```